Outstanding but small benefit administration firm serving large clients needs a website redesign

While the content on our current website is fine, when people arrive at our website, they know immediately that it was designed years ago. We are looking for something that can potentially be maintained on a content management system because we would like to hire a google certified expert to help with adwords and they often want to change the website or add meta data. We want the design to be mobile device friendly.

As for our company, we stress data accuracy, client customization and outstanding customer service. All of our competitors are large corporations (Corvellan, Tolbin, Qualix, PerkWaypoint, etc.). When we get a client, they stay with us. So many of our competitors do a horrible job with administration that many companies just think that's the way it is in this industry. We need to change that thinking! There is someone who can do it right at a reasonable price. We have very few out of scope fees. RMT knows how to make the transition from one administrator to us as painless as possible.

We like our current colors. We don't have a lot of time to write additional content.

Target Market(s)

Companies with 5,000 to 50,000 employees

Coding

Coded - Design and coding required

Number of Pages Required

2 page

Font styles to use
Sans Serif

Requirements
Must have
• If everything doesn't fit on one page, please show me what the second page would look like. For example, if there are See More links, what happens?
• We need for people to be able to submit short contact us with their company name as a required field.
• Ideally this website will be put on wordpress or something similar.
• Must be mobile device friendly.
Should not have
• Login, Register, Maps of our location, website search

```html
<!DOCTYPE html>
<html lang="en">
<head>
<meta charset="utf-8">
<title>Ridgeline Member Trust</title>
<link href="https://fonts.googleapis.com/css2?family=Cinzel:wght@400;700&family=Lato:wght@400;700&family=Open+Sans:wght@300;400&display=swap" rel="stylesheet">
<style>
:root{
  --green:#6fb83f;
  --green-dark:#5aa22e;
  --lime:#b6d22c;
  --blue:#35aee4;
  --ink:#1d1d1d;
  --text:#3c3c3c;
  --muted:#7a7a7a;
  --rule:#cfcfcf;
  --footer:#262626;
  --paper:#ffffff;
}
*{box-sizing:border-box;margin:0;padding:0}
html,body{width:1200px;height:2362px;overflow:hidden;background:var(--paper)}
body{position:relative;font-family:'Lato',sans-serif;color:var(--text)}
.abs{position:absolute}

/* header */
.topline{left:0;top:0;width:1200px;height:5px;background:#2b2b2b}
.site-header{left:0;top:5px;width:1200px;height:92px;background:linear-gradient(#fff,#f1f1f1)}
.brand{left:108px;display:flex;align-items:center;gap:12px}
.brand-dot{width:30px;height:30px;border-radius:50%;background:var(--green)}
.brand-name{font-family:'Open Sans',sans-serif;font-weight:400;font-size:26px;color:#5d5d5d}
.contact-chip{display:flex;align-items:center;gap:12px}
.contact-chip .label{font-weight:700;font-size:13px;color:var(--ink)}
.contact-chip .value{font-size:15px;color:#555;margin-top:2px}
.contact-chip .value.small{font-size:13px}

/* nav */
.main-nav{left:0;top:97px;width:1200px;height:41px;background:linear-gradient(var(--green),var(--green-dark));display:flex;align-items:center;padding-left:110px}
.main-nav a{font-family:'Cinzel',serif;font-size:13px;font-weight:700;color:#fff;text-decoration:none;height:100%;display:flex;align-items:center;justify-content:center;border-right:1px solid rgba(255,255,255,.25)}
.main-nav a.active{background:var(--lime);height:33px;margin-top:-4px;border:none}

/* hero */
.hero{left:0;top:138px;width:1200px;height:471px;
  background:
    radial-gradient(ellipse 260px 160px at 600px 420px,rgba(255,255,255,.95),rgba(255,255,255,0)),
    radial-gradient(ellipse 120px 220px at 930px 260px,rgba(70,80,110,.55),rgba(70,80,110,0)),
    radial-gradient(ellipse 140px 110px at 610px 300px,rgba(60,45,40,.45),rgba(60,45,40,0)),
    radial-gradient(ellipse 160px 120px at 120px 420px,rgba(80,95,120,.5),rgba(80,95,120,0)),
    radial-gradient(ellipse 120px 100px at 1030px 450px,rgba(220,190,150,.55),rgba(220,190,150,0)),
    linear-gradient(90deg,#dfe8e6 0%,#f4f6f2 15%,#cfd9d6 30%,#f6f8f6 45%,#d5dedc 62%,#f3f5f3 78%,#e4eae9 100%)}
.hero-tag{left:106px;font-family:'Cinzel',serif;color:#fff;padding:0 10px;display:flex;align-items:center}
.hero-tag.one{top:352px;height:36px;background:var(--blue);font-size:17px}
.hero-tag.two{top:393px;height:37px;background:var(--green);font-size:20px}
.hero-arrow{top:352px;width:46px;height:46px;border-radius:50%;background:#fff;display:flex;align-items:center;justify-content:center}

/* section headings */
.section-title{left:0;width:1200px;text-align:center;font-family:'Cinzel',serif;font-weight:400;font-size:36px;color:var(--ink)}
.section-title span{color:var(--green)}
.divider{left:310px;width:580px;height:14px}
.divider::before{content:"";position:absolute;left:0;right:0;top:6px;height:1px;background:var(--rule)}
.divider::after{content:"";position:absolute;left:284px;top:1px;width:12px;height:12px;border-radius:50%;background:var(--green)}
.on-green .divider::before{background:rgba(255,255,255,.5)}
.on-green .divider::after{background:#d7efc3}

/* welcome */
.welcome-copy{left:100px;top:744px;width:1000px;text-align:center;font-size:13px;line-height:26px;color:#444}
.feature{top:876px;display:flex;align-items:center;gap:14px}
.feature-icon{width:64px;height:64px;border-radius:50%;background:#e4e4e4;display:flex;align-items:center;justify-content:center}
.feature h3{font-weight:400;font-size:19px;color:var(--ink)}
.feature p{font-size:11.5px;line-height:15px;color:#555;margin-top:3px;width:140px}

/* services */
.services{left:0;top:988px;width:1200px;height:495px;
  background:
    radial-gradient(ellipse 300px 380px at 960px 200px,rgba(60,110,30,.35),rgba(60,110,30,0)),
    radial-gradient(ellipse 260px 300px at 560px 220px,rgba(40,90,25,.25),rgba(40,90,25,0)),
    linear-gradient(110deg,#82c357 0%,#71b845 40%,#64ac39 65%,#7dbf50 85%,#5fa834 100%)}
.service{top:1127px;width:276px;color:#fff;text-align:center}
.service-photo{width:274px;height:137px;border-bottom:5px solid var(--green-dark)}
.service h3{font-family:'Cinzel',serif;font-weight:700;font-size:18px;line-height:19px;margin-top:24px;color:#1f2a14}
.service p{font-size:13px;line-height:22px;margin-top:10px}
.read-more{display:flex;align-items:center;gap:12px;margin-top:14px;font-family:'Cinzel',serif;font-size:13px;font-weight:700}
.read-more::before,.read-more::after{content:"";flex:1;height:1px;background:#fff}

/* testimonials */
.quote{top:1660px;display:flex;gap:24px}
.avatar{width:88px;height:88px;border-radius:50%;border:3px solid var(--green);flex:none;position:relative}
.avatar::after{content:"";position:absolute;left:10px;top:100px;width:68px;height:6px;border-radius:50%;background:rgba(0,0,0,.12)}
.quote-body{width:310px;font-size:13px;line-height:20px;color:#333}
.quote-body .mark{display:inline-block;height:14px;font-family:Georgia,serif;font-weight:700;color:#c9c9c9;font-size:30px;line-height:26px;vertical-align:top;margin:0 2px}
.quote-body .name{font-weight:700;font-size:13px;color:var(--ink);margin-top:12px}
.slider-line{left:172px;top:1831px;width:856px;height:2px;background:#e0e0e0}
.slider-line::after{content:"";position:absolute;left:452px;right:0;top:0;height:2px;background:#777}
.slider-btn{top:1818px;width:28px;height:28px;border-radius:50%;display:flex;align-items:center;justify-content:center}

/* contact */
.contact{left:0;top:1888px;width:1200px;height:380px;background:linear-gradient(135deg,#f3f3f3,#dcdcdc 55%,#ebebeb)}
.sub-title{font-family:'Cinzel',serif;font-weight:400;font-size:20px;color:var(--ink)}
.quick-rule{left:106px;top:2056px;width:514px;height:1px;background:#c9c9c9}
.field{background:#fff;border:1px solid #e3e3e3;font-style:italic;font-size:12px;color:#8a8a8a;padding:10px}
.submit{left:376px;top:2181px;width:241px;height:37px;background:var(--blue);color:#fff;font-family:'Cinzel',serif;font-size:14px;display:flex;align-items:center;justify-content:center}
.col-rule{left:699px;top:2020px;width:2px;height:210px;background:linear-gradient(transparent,#c2c2c2,transparent)}
.info{left:758px;display:flex;gap:22px}
.info h4{font-family:'Cinzel',serif;font-weight:400;font-size:18px;color:var(--ink)}
.info p{font-size:15px;line-height:20px;color:#333}
.info p.strong{font-weight:700;font-size:17px}

/* footer */
.site-footer{left:0;top:2268px;width:1200px;height:50px;background:var(--footer);display:flex;align-items:center;padding-left:110px}
.site-footer a{font-family:'Cinzel',serif;font-size:13px;color:#ddd;text-decoration:none}
.site-footer .sep{width:1px;height:14px;background:#888;margin:0 26px}
.social{top:2280px;left:960px;display:flex;gap:8px}
.social span{width:28px;height:28px;border-radius:50%;background:var(--green);border:2px solid #fff}
.copyright{left:108px;top:2332px;font-size:13px;color:#222}
.to-top{left:1060px;top:2326px;width:26px;height:26px;border-radius:50%;background:#999;display:flex;align-items:center;justify-content:center}
</style>
</head>
<body>

<div class="abs topline"></div>
<header class="abs site-header">
  <div class="abs brand" style="top:19px">
    <span class="brand-dot"></span>
    <span class="brand-name">Ridgeline Member Trust</span>
  </div>
  <div class="abs contact-chip" style="left:697px;top:25px">
    <svg width="36" height="42" viewBox="0 0 36 42"><circle cx="18" cy="21" r="16" fill="none" stroke="#6fb83f" stroke-width="2.5"/><path d="M12 12c-2 2-2 6 1 11s7 8 10 8l3-3-4-4-2 2c-2-1-4-3-5-5l2-2-4-4z" fill="#6fb83f"/></svg>
    <div><div class="label">CALL US :</div><div class="value">555-014-2870</div></div>
  </div>
  <div class="abs contact-chip" style="left:870px;top:25px">
    <svg width="40" height="40" viewBox="0 0 40 40"><rect x="3" y="8" width="34" height="24" fill="none" stroke="#6fb83f" stroke-width="2.5"/><path d="M3 8l17 14 17-14" fill="none" stroke="#6fb83f" stroke-width="2.5"/></svg>
    <div><div class="label">MAIL US :</div><div class="value small">info@ridgelinemember.com</div></div>
  </div>
</header>

<nav class="abs main-nav">
  <a class="active" href="#" style="width:103px">HOME</a>
  <a href="#" style="width:180px">WHY RMT</a>
  <a href="#" style="width:154px">SERVICES</a>
  <a href="#" style="width:170px">TECHNOLOGY</a>
  <a href="#" style="width:188px">CASE STUDIES</a>
  <a href="#" style="width:150px;border:none">CONTACT US</a>
</nav>

<section class="abs hero" role="img" aria-label="Photo of a team meeting in a bright office with tall windows, a man standing and presenting to colleagues around a white table"></section>
<div class="abs hero-tag one">SMALL BENEFIT ADMINISTRATION FIRM</div>
<div class="abs hero-tag two">SERVING LARGE CLIENTS</div>
<div class="abs hero-arrow" style="left:36px"><svg width="14" height="14" viewBox="0 0 14 14"><path d="M9 2L4 7l5 5" fill="none" stroke="#111" stroke-width="3"/></svg></div>
<div class="abs hero-arrow" style="left:1122px"><svg width="14" height="14" viewBox="0 0 14 14"><path d="M5 2l5 5-5 5" fill="none" stroke="#111" stroke-width="3"/></svg></div>

<h1 class="abs section-title" style="top:666px">Welcome to <span>Ridgeline Member Trust</span></h1>
<div class="abs divider" style="top:716px"></div>
<p class="abs welcome-copy">Sed ut perspiciatis unde omnis iste natus error sit voluptatem accusantium dolo remque laudantium, totam rem aperiam, eaque ipsa quae ab illo inventore veritatis et quasi architecto beatae vitae dicta sunt explicabo. Sed ut perspiciatis unde omnis isusantium dolo remque laudantium, totam rem aperiam, eaque ipsa quae ab illo inventore veritatis et quasi architecto beatae vitae dicta sunt explicabo. Sed ut perspiciatis unde omnis iste natus error sit voluptatem accusantium dolo. Ste natus error sit voluptatem accusantium dolo.antium dolo.Sed ut perspiciatis unde omnis iste natus error sit voluptatem accusantium dolo.</p>

<div class="abs feature" style="left:340px">
  <div class="feature-icon"><svg width="34" height="30" viewBox="0 0 34 30"><circle cx="9" cy="8" r="5" fill="#333"/><circle cx="25" cy="8" r="5" fill="#333"/><path d="M1 24c0-6 4-9 8-9s8 3 8 9z M17 24c0-6 4-9 8-9s8 3 8 9z" fill="#6fb83f"/><circle cx="17" cy="14" r="5" fill="#333"/><path d="M8 30c0-6 4-9 9-9s9 3 9 9z" fill="#333"/></svg></div>
  <div><h3>Who We Are</h3><p>Sed ut perspiciatis unde omnis iste natus .</p></div>
</div>
<div class="abs feature" style="left:614px">
  <div class="feature-icon"><svg width="32" height="34" viewBox="0 0 32 34"><path d="M8 32v-7c-4-3-6-7-5-12C5 5 12 2 18 3c6 1 10 6 10 12l3 5-3 1v5c0 2-2 3-4 3h-3v3" fill="none" stroke="#333" stroke-width="2.2"/><circle cx="16" cy="14" r="4" fill="none" stroke="#6fb83f" stroke-width="2.2"/></svg></div>
  <div><h3>Our Philosophy</h3><p>Sed ut perspiciatis unde omnis iste natus .</p></div>
</div>

<section class="abs services" role="img" aria-label="Green tinted photo of business people working at a desk"></section>
<div class="on-green">
  <h2 class="abs section-title" style="top:1016px;color:#fff">Our Services</h2>
  <div class="abs divider" style="top:1070px"></div>
</div>

<article class="abs service" style="left:106px">
  <div class="service-photo" role="img" aria-label="Photo of two colleagues reviewing a bar chart on a monitor" style="background:radial-gradient(ellipse 50px 60px at 70px 85px,rgba(40,40,50,.7),rgba(40,40,50,0)),linear-gradient(90deg,#eef2f6 0%,#dfe6ee 45%,#2a2f36 58%,#47617e 80%,#2b3138 100%)"></div>
  <h3>H &amp; W<br>Administration</h3>
  <p>Lorem ipsum dolouar sit amet consecinventore veritatis et quasi arvitae dictam.</p>
  <div class="read-more">READ MORE</div>
</article>
<article class="abs service" style="left:455px">
  <div class="service-photo" role="img" aria-label="Photo of a business team gathered around a laptop" style="background:radial-gradient(ellipse 60px 50px at 200px 60px,rgba(225,195,160,.8),rgba(225,195,160,0)),radial-gradient(ellipse 70px 40px at 90px 110px,rgba(220,220,225,.8),rgba(220,220,225,0)),linear-gradient(135deg,#5a5a5e,#222428 60%,#3a3c40)"></div>
  <h3>Defined<br>Benefit Administration</h3>
  <p>Lorem ipsum dolouar sit amet consecinventore veritatis et quasi arvitae dictam.</p>
  <div class="read-more">READ MORE</div>
</article>
<article class="abs service" style="left:806px">
  <div class="service-photo" role="img" aria-label="Photo of hands pointing at printed charts on a table" style="background:radial-gradient(ellipse 80px 30px at 200px 20px,rgba(40,45,55,.75),rgba(40,45,55,0)),linear-gradient(160deg,#dfe3e6 0%,#f7f8f8 45%,#c9ced3 100%)"></div>
  <h3>Benefit Consulting<br>Services</h3>
  <p>Lorem ipsum dolouar sit amet consecinventore veritatis et quasi arvitae dictam.</p>
  <div class="read-more">READ MORE</div>
</article>

<h2 class="abs section-title" style="top:1550px">Client <span>Testimonial</span></h2>
<div class="abs divider" style="top:1604px"></div>

<div class="abs quote" style="left:148px">
  <div class="avatar" role="img" aria-label="Client portrait" style="background:radial-gradient(circle at 50% 40%,#c8a88c 0 30%,#8a7564 31% 55%,#e4e6e8 56%)"></div>
  <div class="quote-body"><span class="mark">&ldquo;</span>Duis autem vel eum iriure dolor in hendrerit in vulputate velitj esse molestie consequat, vel illum dolore eu feugiat nulla faciln sis at vero eros et accumsan et &nbsp;delenit facilisi.<span class="mark">&rdquo;</span><div class="name">Mr. Alan Pereira</div></div>
</div>
<div class="abs quote" style="left:648px">
  <div class="avatar" role="img" aria-label="Client portrait" style="background:radial-gradient(circle at 50% 42%,#e6c6aa 0 28%,#6b4a35 29% 50%,#eceeef 51%)"></div>
  <div class="quote-body"><span class="mark">&ldquo;</span>Duis autem vel eum iriure dolor in hendrerit in vulputate velitj esse molestie consequat, vel illum dolore eu feugiat nulla faciln sis at vero eros et accumsan et &nbsp;delenit facilisi.<span class="mark">&rdquo;</span><div class="name">Miss Nora Faulk</div></div>
</div>

<div class="abs slider-line"></div>
<div class="abs slider-btn" style="left:579px;background:#d4d4d4"><svg width="10" height="10" viewBox="0 0 10 10"><path d="M7 1L3 5l4 4" fill="none" stroke="#fff" stroke-width="2"/></svg></div>
<div class="abs slider-btn" style="left:612px;background:#222"><svg width="10" height="10" viewBox="0 0 10 10"><path d="M3 1l4 4-4 4" fill="none" stroke="#fff" stroke-width="2"/></svg></div>

<section class="abs contact"></section>
<h2 class="abs section-title" style="top:1916px">Contact <span>Us</span></h2>
<div class="abs divider" style="top:1976px"></div>

<h3 class="abs sub-title" style="left:108px;top:2022px">Quick Contact</h3>
<div class="abs quick-rule"></div>
<div class="abs field" style="left:110px;top:2073px;width:244px;height:37px">Name</div>
<div class="abs field" style="left:110px;top:2130px;width:244px;height:36px">Email</div>
<div class="abs field" style="left:110px;top:2181px;width:244px;height:37px">Phone</div>
<div class="abs field" style="left:376px;top:2073px;width:245px;height:92px">Message</div>
<div class="abs submit">SUBMIT</div>
<div class="abs col-rule"></div>

<div class="abs info" style="top:2026px">
  <svg width="16" height="20" viewBox="0 0 16 20"><path d="M8 1a6 6 0 0 0-6 6c0 5 6 11 6 11s6-6 6-11a6 6 0 0 0-6-6z" fill="#111"/><circle cx="8" cy="7" r="2.2" fill="#eee"/></svg>
  <div><h4>Address Information</h4><p>4820 Larkfield Ave<br>Westbrook Twp., MI 48000</p></div>
</div>
<div class="abs info" style="top:2106px">
  <svg width="18" height="14" viewBox="0 0 18 14" style="margin-top:4px"><rect x="1" y="1" width="16" height="12" fill="#111"/><path d="M1 1l8 7 8-7" fill="none" stroke="#eee" stroke-width="1.4"/></svg>
  <div><h4>Email</h4><p>info@ridgelinemember.com</p></div>
</div>
<div class="abs info" style="top:2174px">
  <svg width="16" height="16" viewBox="0 0 16 16" style="margin-top:4px"><path d="M3 1c-2 2-2 5 1 9s6 6 9 5l2-2-3-3-2 1c-2-1-3-3-4-4l1-2-3-3z" fill="#111"/></svg>
  <div><h4>Call Us</h4><p class="strong">555-014-2870</p></div>
</div>

<footer class="abs site-footer">
  <a href="#">Home</a><span class="sep"></span>
  <a href="#">Why RMT</a><span class="sep"></span>
  <a href="#">Services</a><span class="sep" style="margin:0 36px"></span>
  <a href="#">Technology</a><span class="sep" style="margin:0 36px"></span>
  <a href="#">Contact Us</a>
</footer>
<div class="abs social" aria-label="Social links"><span></span><span></span><span></span><span></span></div>
<p class="abs copyright">Copyright @ 2016 &nbsp;Ridgelinemember, All Rights Reserved</p>
<div class="abs to-top"><svg width="12" height="12" viewBox="0 0 12 12"><path d="M6 10V2M2 6l4-4 4 4" fill="none" stroke="#fff" stroke-width="2"/></svg></div>

</body>
</html>
```